Logo-Design für Alterswohnungen
Zielgruppe
Die Alterswohnungen Fennrüti AG ist eine Kapitalgesellschaft im Besitz der Gemeinde Dättlikon und erstellt für die Gemeinde einen Neubau mit Alterswohnungen und verwaltet und betreibt diese. Der Name Alterswohnungen Fennrüti AG oder die Abkürzung AWFAG wurden als Domain registriert, müssen jedoch nicht extrem hervor gestrichen werden, möglich ist auch, dass für das vermutlich 2019 fertig gestellte Objekt ein eigener Name gesucht wird. Im Moment sind wir in der Projektierungsphase und gehen davon aus, dass der Baubeginn im Frühjahr 2019 ist.
Aufgabenstellung
Es ist nicht vorgesehen, grosse Druckaufträge zu erteilen, die meisten Druckerzeugnisse werden inhouse auf den Laserdruckern erstellt. Das CD soll jedoch ansprechend sein und einfach und schnell für alle Vorlagen eingesetzt werden können.

```html
<!DOCTYPE html>
<html lang="de">
<head>
<meta charset="utf-8">
<title>Alterswohnungen Fennrüti AG – Erscheinungsbild</title>
<link rel="stylesheet" href="https://fonts.googleapis.com/css2?family=Roboto:wght@300;400&display=swap">
<style>
  :root {
    --ink: #111114;
    --mark-grey: #c3c3cb;
    --band-grey: #a2a4ad;
    --paper: #ffffff;
    --fold-mark: #9a6f82;
    --shadow: rgba(0,0,0,0.35);
  }
  html, body { margin: 0; padding: 0; }
  body {
    width: 1200px; height: 2587px; overflow: hidden;
    background: var(--paper);
    position: relative;
    font-family: "Roboto", "Helvetica Neue", Arial, sans-serif;
    font-weight: 300;
    color: var(--ink);
  }
  .abs { position: absolute; }

  /* logo lockup: name text, divider, plain square */
  .lockup-name {
    position: absolute; text-align: right; white-space: nowrap;
    letter-spacing: 0.14em; line-height: 1.1; margin: 0; font-weight: 300;
  }
  .lockup-name span { display: block; }
  .lockup-divider { position: absolute; width: 1px; background: var(--mark-grey); }
  .lockup-square { position: absolute; border: 1.5px solid var(--mark-grey); box-sizing: border-box; border-radius: 4px; }
  .lockup--black .lockup-divider { background: #7c7c80; }
  .lockup--black .lockup-square { border-color: var(--ink); }

  .sheet {
    position: absolute; background: var(--paper);
    box-shadow: 8px 8px 10px var(--shadow);
    outline: 1px solid #e2e2e4;
  }

  .card-band {
    position: absolute; left: 0; right: 0; bottom: 0; height: 91px;
    background: var(--band-grey); color: #fff; text-align: center;
    font-size: 16px; letter-spacing: 0.1em; line-height: 21px; font-weight: 400;
    padding-top: 10px; box-sizing: border-box;
  }
  .card-person { position: absolute; left: 37px; top: 160px; letter-spacing: 0.14em; font-size: 18px; font-weight: 400; }
  .card-role { position: absolute; left: 37px; top: 184px; letter-spacing: 0.1em; font-size: 13px; font-weight: 400; }

  .fold-mark { position: absolute; left: 0; width: 23px; height: 1px; background: var(--fold-mark); }
  .sender-line { position: absolute; left: 171px; top: 268px; font-size: 13.5px; letter-spacing: 0.06em; line-height: 17px; font-weight: 400; }
  .sender-square { position: absolute; left: 130px; top: 268px; width: 30px; height: 33px; border: 1px solid var(--mark-grey); box-sizing: border-box; border-radius: 2px; }
  .address-block { position: absolute; left: 875px; top: 262px; font-size: 17px; letter-spacing: 0.1em; line-height: 22px; font-weight: 400; }
  .address-block p { margin: 0 0 6px; }
</style>
</head>
<body>

  <!-- primary lockup -->
  <div class="lockup">
    <p class="lockup-name" style="right:400px; top:130px; font-size:74px; line-height:79px;"><span>Alterswohnungen</span><span>Fennrüti AG</span></p>
    <div class="lockup-divider" style="left:860px; top:24px; height:260px;"></div>
    <div class="lockup-square" style="left:924px; top:24px; width:221px; height:261px;"></div>
  </div>

  <!-- business card front -->
  <div class="sheet" style="left:44px; top:431px; width:489px; height:308px;">
    <p class="lockup-name" style="right:163px; top:124px; font-size:29px; line-height:29px;"><span>Alterswohnungen</span><span>Fennrüti AG</span></p>
    <div class="lockup-divider" style="left:346px; top:84px; height:97px;"></div>
    <div class="lockup-square" style="left:372px; top:84px; width:81px; height:97px;"></div>
  </div>

  <!-- business card back -->
  <div class="sheet" style="left:653px; top:431px; width:491px; height:308px;">
    <p class="lockup-name" style="right:124px; top:64px; font-size:22px; line-height:22px;"><span>Alterswohnungen</span><span>Fennrüti AG</span></p>
    <div class="lockup-divider" style="left:381px; top:39px; height:69px;"></div>
    <div class="lockup-square" style="left:397px; top:39px; width:60px; height:69px;"></div>
    <div class="card-person">Reto Kobelmatt</div>
    <div class="card-role">VRP / Geschäftsführer</div>
    <div class="card-band">
      Lindenweg 4, 8425 Fennrüti<br>
      Mobile +41 79 512 08 47<br>
      r.kobelmatt@awfag.ch www.awfag.ch
    </div>
  </div>

  <!-- black lockup -->
  <div class="lockup lockup--black">
    <p class="lockup-name" style="right:500px; top:876px; font-size:44px; line-height:40px;"><span>Alterswohnungen</span><span>Fennrüti AG</span></p>
    <div class="lockup-divider" style="left:731px; top:824px; height:133px;"></div>
    <div class="lockup-square" style="left:761px; top:824px; width:116px; height:133px;"></div>
  </div>

  <!-- letterhead -->
  <div class="sheet" style="left:40px; top:1002px; width:1107px; height:1564px;">
    <p class="lockup-name" style="right:187px; top:104px; font-size:31px; line-height:28px;"><span>Alterswohnungen</span><span>Fennrüti AG</span></p>
    <div class="lockup-divider" style="left:939px; top:71px; height:91px;"></div>
    <div class="lockup-square" style="left:961px; top:71px; width:78px; height:91px;"></div>

    <div class="sender-square"></div>
    <div class="sender-line">Alterswohnungen Fennrüti AG<br>Lindenweg 4 · 8425 Fennrüti</div>

    <div class="address-block">
      <p>Alterswohnungen<br>Fennrüti AG</p>
      <p>c/o Gemeinde<br>Fennrüti</p>
      <p>Lindenweg 4<br>8425 Fennrüti</p>
      <p>info@awfag.ch<br>www.awfag.ch</p>
    </div>

    <div class="fold-mark" style="top:486px;"></div>
    <div class="fold-mark" style="top:780px;"></div>
  </div>

</body>
</html>
```